I need a business card design for a new company that will be doing consulting work around issues of cultural competency, and diversity and inclusion. I would like the design to be crisp and clear with bold but conservative colors and incorporate shades of blue

Target Market(s)

Small businesses, schools, non-profits

Industry/Entity Type

Consulting

Font styles to use
Serif
Sans Serif

Colors
0c5ba6
6b449b
3276b5
0292cd

Requirements
Must have
• A Morrow Venture (name of company)
• Lemlem Tavish
• CEO
• lemlem@amorrowventure.com
• (215)483-2756

```html
<!DOCTYPE html>
<html lang="en">
<head>
<meta charset="utf-8">
<title>A Morrow Venture — Business Card</title>
<link rel="stylesheet" href="https://fonts.googleapis.com/css2?family=Roboto+Condensed:wght@400;700&family=Roboto:wght@300;400&display=swap">
<style>
  :root {
    --backdrop: #3b86c2;
    --card-white: #ffffff;
    --navy: #02589a;
    --name-blue: #0a569b;
    --email-band: #0571b0;
    --phone-band: #6796c5;
    --text-light: #ffffff;
  }
  * { margin: 0; padding: 0; box-sizing: border-box; }
  html, body {
    width: 1200px;
    height: 820px;
    overflow: hidden;
    background: var(--backdrop);
  }
  .business-card {
    position: absolute;
    left: 228px;
    top: 201px;
    width: 745px;
    height: 419px;
    background: var(--card-white);
    overflow: hidden;
  }
  .card-shapes {
    position: absolute;
    inset: 0;
  }
  .holder-name {
    position: absolute;
    left: 84px;
    top: 92px;
    width: 250px;
    font-family: "Roboto Condensed", sans-serif;
    font-size: 41px;
    line-height: 1;
    color: var(--name-blue);
    white-space: nowrap;
  }
  .holder-name .given { font-weight: 700; }
  .holder-name .family { font-weight: 400; }
  .holder-role {
    position: absolute;
    left: 148px;
    top: 131px;
    font-family: "Roboto", sans-serif;
    font-weight: 300;
    font-size: 20px;
    letter-spacing: 0.55em;
    color: var(--name-blue);
    line-height: 1;
  }
  .contact-email,
  .contact-phone {
    position: absolute;
    left: 0;
    width: 412px;
    text-align: center;
    font-family: "Roboto", sans-serif;
    font-weight: 300;
    color: var(--text-light);
    line-height: 1;
  }
  .contact-email { top: 181px; font-size: 20px; }
  .contact-phone { top: 221px; font-size: 24px; }
  .company-wordmark {
    position: absolute;
    left: 428px;
    top: 172px;
    width: 304px;
    text-align: center;
    font-family: "Roboto Condensed", sans-serif;
    font-weight: 700;
    color: var(--text-light);
    line-height: 1;
  }
  .company-wordmark .line-main {
    display: block;
    font-size: 56px;
    letter-spacing: 0.13em;
    margin-right: -0.13em;
  }
  .company-wordmark .line-sub {
    display: block;
    margin-top: 2px;
    font-size: 26px;
    letter-spacing: 0.45em;
    margin-right: -0.45em;
  }
</style>
</head>
<body>
  <div class="business-card">
    <svg class="card-shapes" width="745" height="419" viewBox="0 0 745 419" aria-hidden="true">
      <rect class="email-band" x="0" y="170" width="745" height="42" fill="var(--email-band)"/>
      <rect class="phone-band" x="0" y="212" width="745" height="43" fill="var(--phone-band)"/>
      <polygon class="corner-wedge" points="0,0 76,0 0,143" fill="var(--navy)"/>
      <polygon class="brand-panel" points="521,0 745,0 745,419 296,419" fill="var(--navy)"/>
    </svg>

    <h1 class="holder-name"><span class="given">LEMLEM</span> <span class="family">TAVISH</span></h1>
    <p class="holder-role">CEO</p>
    <p class="contact-email">LEMLEM@AMORROWVENTURE.COM</p>
    <p class="contact-phone">(215)483-2756</p>

    <p class="company-wordmark">
      <span class="line-main">AMORROW</span>
      <span class="line-sub">VENTURE</span>
    </p>
  </div>
</body>
</html>
```